Promotion Banner on Website Homepage

Needing a four designs for our website homepage. our web address is: www.brisktailcourier.com
I like the colors used for the current banners that came stock with the website. And I like that the whole banner is not solid in color or graphic.
The four designs we need will take the place of the four images calling attention to the sale items.
Each banner final size is 228 x 228 pixels.
Specifics for each banner are as follows:
1. (Text) Made in Wisconsin (Image) State of Wisconsin outline in the back with the text over it.
2. (Text) The most awarded pet food (Image) Valmora is the brand that this will relate to. Can use the company logo or use an image of their Adult dog food from their website at: www.valmora.ca
3. (Text) Bulk Treats, get up to 25% off (image) (open to options)
4. (Text) 100% Natural. No Preservatives. No Additives. Authentic. Corvale Pup Gnaw. (image) (open to options)
Industry/Entity Type
Pet
Requirements
Must have
- Should use the same colors that are currently used on the banners that I wish to replace.
Green, orange, blue.
Should not have
- Do not include paws, graphics that do not relate to the message of the banner. Should not be 'heavy' feeling.

```html
<!DOCTYPE html>
<html lang="en">
<head>
<meta charset="utf-8">
<title>Homepage Promotion Badges</title>
<link href="https://fonts.googleapis.com/css2?family=Open+Sans:wght@400;600;700;800&display=swap" rel="stylesheet">
<style>
  :root {
    --bg: #ffffff;
    --orange-light: #f9a13a;
    --orange: #f27a21;
    --orange-deep: #e0561a;
    --green-light: #9bd233;
    --green: #5fae1e;
    --green-deep: #2f7a12;
    --green-shadow: #1f5a0c;
    --white: #ffffff;
    --map-light: #eeeff1;
    --map-grey: #cfd2d6;
  }
  * { box-sizing: border-box; margin: 0; padding: 0; }
  html, body { width: 1200px; height: 367px; overflow: hidden; background: var(--bg); }
  body { font-family: "Open Sans", Arial, sans-serif; position: relative; }

  .badge { position: absolute; top: 34px; width: 260px; height: 300px; }
  .badge--made    { left: 18px; }
  .badge--awarded { left: 316px; }
  .badge--bulk    { left: 615px; }
  .badge--natural { left: 914px; }

  .badge__art { position: absolute; inset: 0; width: 260px; height: 300px; }
  .badge__art--front { z-index: 2; pointer-events: none; }

  .badge__title {
    position: absolute; z-index: 3; left: 44px; top: 22px; width: 190px;
    color: var(--white); font-weight: 700; font-size: 14px; line-height: 17px;
    text-transform: uppercase; letter-spacing: -0.2px;
    text-shadow: 0 1px 1px rgba(0,0,0,.25);
  }
  .badge__title--two-line { top: 18px; }

  .badge__visual { position: absolute; z-index: 1; border-radius: 6px; }
  .state-map {
    left: 54px; top: 82px; width: 150px; height: 132px;
    background: linear-gradient(160deg, var(--map-light), var(--map-grey));
  }
  .product-scene {
    left: 34px; top: 78px; width: 196px; height: 140px;
    background: linear-gradient(90deg, #b8492c 0%, #8a3a2a 35%, #c89058 60%, #d8a86c 100%);
  }

  .deal { position: absolute; left: 26px; top: 82px; width: 206px; text-align: center; color: var(--white); }
  .deal__rule {
    display: flex; align-items: center; justify-content: center; gap: 8px;
    font-weight: 700; font-size: 15px; letter-spacing: .3px;
  }
  .deal__rule::before, .deal__rule::after {
    content: ""; width: 22px; height: 1.5px; background: var(--white);
  }
  .deal__amount { font-weight: 700; font-size: 62px; line-height: 78px; letter-spacing: -1px; }
  .deal__amount sup { font-size: 22px; font-weight: 600; vertical-align: 28px; margin-left: 4px; }

  .claims {
    position: absolute; left: 26px; top: 106px; width: 206px; text-align: center;
    color: var(--white); font-weight: 700; font-size: 17px; line-height: 25px;
    text-shadow: 0 1px 1px rgba(0,0,0,.2);
  }
</style>
</head>
<body>

<svg width="0" height="0" style="position:absolute" aria-hidden="true">
  <defs>
    <linearGradient id="tileFill" x1="0" y1="0" x2="0" y2="1">
      <stop offset="0" stop-color="var(--orange-light)"/>
      <stop offset=".55" stop-color="var(--orange)"/>
      <stop offset="1" stop-color="var(--orange-deep)"/>
    </linearGradient>
    <linearGradient id="ribbonFill" x1="0" y1="0" x2="1" y2="1">
      <stop offset="0" stop-color="var(--green-deep)"/>
      <stop offset=".45" stop-color="var(--green)"/>
      <stop offset="1" stop-color="var(--green-light)"/>
    </linearGradient>
    <linearGradient id="ribbonLower" x1="0" y1="0" x2="1" y2="0">
      <stop offset="0" stop-color="var(--green-deep)"/>
      <stop offset=".5" stop-color="var(--green-light)"/>
      <stop offset="1" stop-color="var(--green)"/>
    </linearGradient>
    <g id="badgeTile">
      <rect x="26" y="44" width="206" height="212" rx="20" fill="url(#tileFill)"/>
    </g>
    <g id="badgeRibbons">
      <path d="M232 54 L254 44 L250 78 L232 70 Z" fill="var(--green-shadow)"/>
      <path d="M38 14 L236 10 Q248 36 252 64 L44 70 Q40 40 38 14 Z" fill="url(#ribbonFill)"/>
      <path d="M38 14 L28 40 L44 70 Z" fill="var(--green-deep)"/>
      <path d="M2 230 L22 226 L30 262 L10 268 Z" fill="var(--green-shadow)"/>
      <path d="M14 214 Q120 262 246 246 L252 286 Q120 300 22 256 Z" fill="url(#ribbonLower)"/>
      <path d="M60 248 Q140 272 230 262" stroke="rgba(255,255,255,.35)" stroke-width="3" fill="none"/>
    </g>
  </defs>
</svg>

<section class="badge badge--made">
  <svg class="badge__art" viewBox="0 0 260 300"><use href="#badgeTile"/></svg>
  <div class="badge__visual state-map" role="img" aria-label="Outline map of the state of Wisconsin with county borders"></div>
  <svg class="badge__art badge__art--front" viewBox="0 0 260 300"><use href="#badgeRibbons"/></svg>
  <h2 class="badge__title">Made in Wisconsin</h2>
</section>

<section class="badge badge--awarded">
  <svg class="badge__art" viewBox="0 0 260 300"><use href="#badgeTile"/></svg>
  <div class="badge__visual product-scene" role="img" aria-label="Valmora dog food bags beside a seated tan dog"></div>
  <svg class="badge__art badge__art--front" viewBox="0 0 260 300"><use href="#badgeRibbons"/></svg>
  <h2 class="badge__title badge__title--two-line">The most<br>awarded pet food</h2>
</section>

<section class="badge badge--bulk">
  <svg class="badge__art" viewBox="0 0 260 300"><use href="#badgeTile"/></svg>
  <svg class="badge__art badge__art--front" viewBox="0 0 260 300"><use href="#badgeRibbons"/></svg>
  <h2 class="badge__title">Bulk Treats</h2>
  <div class="deal">
    <p class="deal__rule">GET UP TO</p>
    <p class="deal__amount">25<sup>%</sup></p>
    <p class="deal__rule">OFF</p>
  </div>
</section>

<section class="badge badge--natural">
  <svg class="badge__art" viewBox="0 0 260 300"><use href="#badgeTile"/></svg>
  <svg class="badge__art badge__art--front" viewBox="0 0 260 300"><use href="#badgeRibbons"/></svg>
  <h2 class="badge__title">100% Natural.</h2>
  <p class="claims">No Preservatives.<br>No Additives.<br>Authentic.<br>Corvale Pup Gnaw.</p>
</section>

</body>
</html>
```